Book & e-book cover - front, back and sleeve

Please see plot description:

The Lantern

A man lies dying and trapped in a parking garage stairwell. The poorly lit stairwell serves as a painful reminder of one of his memories of childhood locked in that darkened closet. To keep himself in tact he would play with a shiny silver button he ripped off from his pajamas – throwing it in the air and tapping the floor to find it. As he lies trapped and dying that same defeated and abandoned feeling descends upon him. As he comes in and out of consciousness memories from his past manifest themselves and we are introduced to the turbulent and sometimes triumphant pathway that has led him to his current state. It is up to him to sort through the barrage of emotions to find his way out, to let go, to forgive. That is if his heart will let him.
Updates

I know that we mentioned having a photograph of a button on the cover but we would like to see examples of covers with a more abstract or drawn or painted looking button.  Thanks.

Target Market(s)

Dramatic story - geared towards adult readers

Industry/Entity Type

Parking

Requirements
Must have
• Simple, crisp, custom, classic look. Do not want it to look to sci-fi or medival - this is an emotional story - a memoir.

Items on the front cover:

Title: The Lantern
Author: R.M. Halvorsen
Words: A Novel
Photo: a sliver button (just one image)

Items on the back cover

Plot description area
ISBN area at bottom

Nice to have
• Please see examples that have been uploaded. I like novels with a textured background.

A simple button on the cover with the right fonts and colour scheme.
Should not have
• I do not want a person or icons used on the cover
I do not want it to busy.
Do not want it to feel like it is a sci-fi novel or medival story.
Do not want the cover to be too "dark" - I do not want potential readers to get the wrong idea of what "The Lantern" is about.

```html
<!DOCTYPE html>
<html lang="en">
<head>
<meta charset="utf-8">
<title>The Lantern — cover wrap</title>
<link rel="stylesheet" href="https://fonts.googleapis.com/css2?family=Special+Elite&family=Courier+Prime:ital,wght@0,400;0,700;1,400&display=swap">
<style>
  :root {
    --paper: #e9e7da;
    --ink: #111110;
    --ink-soft: #262624;
    --silver-light: #f6f6f4;
    --silver-mid: #b9bbb8;
    --silver-dark: #6a6c69;
    --isbn-box: #ffffff;
  }
  html, body {
    margin: 0;
    padding: 0;
    width: 1200px;
    height: 891px;
    overflow: hidden;
    background: var(--paper);
  }
  .cover-wrap {
    position: relative;
    width: 1200px;
    height: 891px;
    overflow: hidden;
    background: var(--paper);
  }
  .paper-texture {
    position: absolute;
    left: 0; top: 0;
    width: 1200px; height: 891px;
  }

  /* back cover */
  .back-cover {
    position: absolute;
    left: 0; top: 0;
    width: 575px; height: 891px;
  }
  .back-tagline {
    position: absolute;
    left: 40px; width: 500px;
    top: 296px;
    margin: 0;
    text-align: center;
    font-family: "Courier Prime", "Courier New", monospace;
    font-style: italic;
    font-size: 18px;
    line-height: 28px;
    color: var(--ink-soft);
    filter: url(#ink-rough-fine);
  }
  .isbn-area {
    position: absolute;
    left: 222px; top: 744px;
    width: 135px; height: 76px;
    background: var(--isbn-box);
  }

  /* spine */
  .spine {
    position: absolute;
    left: 575px; top: 0;
    width: 45px; height: 891px;
  }
  .spine-line {
    position: absolute;
    left: 6px; top: 178px;
    writing-mode: vertical-rl;
    display: flex;
    align-items: center;
    gap: 5px;
    color: var(--ink);
    white-space: nowrap;
    filter: url(#ink-rough-fine);
  }
  .spine-title {
    font-family: "Special Elite", "Courier New", monospace;
    font-size: 30px;
    letter-spacing: 1px;
    -webkit-text-stroke: 1px var(--ink);
  }
  .spine-mark {
    width: 17px; height: 17px;
    border-radius: 50%;
    background: var(--silver-mid);
    border: 1px solid var(--ink-soft);
    box-sizing: border-box;
  }
  .spine-author {
    font-family: "Special Elite", "Courier New", monospace;
    font-size: 22px;
    letter-spacing: 1px;
    -webkit-text-stroke: 0.5px var(--ink);
  }

  /* front cover */
  .front-cover {
    position: absolute;
    left: 620px; top: 0;
    width: 580px; height: 891px;
  }
  .front-title {
    position: absolute;
    left: 0; width: 580px;
    top: 62px;
    margin: 0;
    text-align: center;
    white-space: nowrap;
    font-family: "Special Elite", "Courier New", monospace;
    font-weight: 400;
    font-size: 68px;
    line-height: 84px;
    letter-spacing: 1px;
    color: var(--ink);
    -webkit-text-stroke: 2.2px var(--ink);
    text-shadow: 2px 3px 3px rgba(0,0,0,0.3);
    filter: url(#ink-rough);
  }
  .front-subtitle {
    position: absolute;
    left: 0; width: 570px;
    top: 170px;
    margin: 0;
    text-align: center;
    font-family: "Special Elite", "Courier New", monospace;
    font-size: 22px;
    color: var(--ink);
    -webkit-text-stroke: 0.4px var(--ink);
  }
  .button-reflection {
    position: absolute;
    left: 112px; top: 470px;
    width: 350px; height: 170px;
    border-radius: 50%;
    background: radial-gradient(ellipse at 50% 30%, rgba(200,202,199,0.55), transparent 70%);
  }
  .button-art {
    position: absolute;
    left: 104px; top: 262px;
    width: 362px; height: 268px;
    border-radius: 50%;
    background: radial-gradient(ellipse at 45% 35%, var(--silver-light) 0%, var(--silver-mid) 55%, var(--silver-dark) 100%);
  }
  .front-author {
    position: absolute;
    left: 0; width: 570px;
    top: 812px;
    margin: 0;
    text-align: center;
    font-family: "Courier Prime", "Courier New", monospace;
    font-weight: 700;
    font-size: 25px;
    letter-spacing: 3px;
    color: var(--ink-soft);
    filter: url(#ink-rough-fine);
  }
</style>
</head>
<body>
  <main class="cover-wrap">
    <svg class="paper-texture" viewBox="0 0 1200 891" aria-hidden="true">
      <defs>
        <filter id="grey-mottle" x="0" y="0" width="100%" height="100%">
          <feTurbulence type="fractalNoise" baseFrequency="0.006" numOctaves="4" seed="3"/>
          <feColorMatrix type="matrix" values="0 0 0 0 0.62  0 0 0 0 0.63  0 0 0 0 0.60  1.4 0 0 0 -0.62"/>
        </filter>
        <filter id="yellow-stains" x="0" y="0" width="100%" height="100%">
          <feTurbulence type="fractalNoise" baseFrequency="0.018" numOctaves="5" seed="11"/>
          <feColorMatrix type="matrix" values="0 0 0 0 0.72  0 0 0 0 0.70  0 0 0 0 0.30  0 2.6 0 0 -1.32"/>
        </filter>
        <filter id="speckles" x="0" y="0" width="100%" height="100%">
          <feTurbulence type="fractalNoise" baseFrequency="0.75" numOctaves="2" seed="5"/>
          <feColorMatrix type="matrix" values="0 0 0 0 0.42  0 0 0 0 0.42  0 0 0 0 0.30  7 0 0 0 -4.6"/>
        </filter>
        <filter id="ink-rough" x="-5%" y="-10%" width="110%" height="120%">
          <feTurbulence type="fractalNoise" baseFrequency="0.55" numOctaves="2" seed="2" result="grain"/>
          <feDisplacementMap in="SourceGraphic" in2="grain" scale="3" xChannelSelector="R" yChannelSelector="G" result="moved"/>
          <feColorMatrix in="grain" type="matrix" values="0 0 0 0 0  0 0 0 0 0  0 0 0 0 0  -5 0 0 0 3.9" result="holes"/>
          <feComposite in="moved" in2="holes" operator="in"/>
        </filter>
        <filter id="ink-rough-fine" x="-5%" y="-10%" width="110%" height="120%">
          <feTurbulence type="fractalNoise" baseFrequency="0.8" numOctaves="2" seed="9" result="grain"/>
          <feDisplacementMap in="SourceGraphic" in2="grain" scale="1.5" xChannelSelector="R" yChannelSelector="G"/>
        </filter>
      </defs>
      <rect width="1200" height="891" fill="#ebe9de"/>
      <rect width="1200" height="891" filter="url(#grey-mottle)"/>
      <rect width="1200" height="891" filter="url(#yellow-stains)"/>
      <rect width="1200" height="891" filter="url(#speckles)"/>
      <g fill="none" stroke="#9a9a90" stroke-opacity="0.45" stroke-width="1.2">
        <path d="M0 812 C180 800 320 786 470 782 S640 790 780 780 S1020 772 1200 766"/>
        <path d="M620 0 L622 891" stroke-opacity="0.25"/>
        <path d="M160 300 C240 290 320 296 420 288" stroke-opacity="0.3"/>
        <path d="M680 430 C760 424 900 432 1010 426" stroke-opacity="0.25"/>
      </g>
    </svg>

    <section class="back-cover">
      <p class="back-tagline">What will hold Ryan's life together<br>when everything is coming apart</p>
      <div class="isbn-area" aria-label="ISBN area"></div>
    </section>

    <section class="spine">
      <div class="spine-line">
        <span class="spine-title">the lantern</span>
        <span class="spine-mark"></span>
        <span class="spine-author">R.M. HALVORSEN</span>
      </div>
    </section>

    <section class="front-cover">
      <h1 class="front-title">the lantern</h1>
      <p class="front-subtitle">a novel</p>
      <div class="button-reflection" aria-hidden="true"></div>
      <div class="button-art" role="img" aria-label="A shiny silver four-hole button with a soft reflection beneath it"></div>
      <p class="front-author">R. M. HALVORSEN</p>
    </section>
  </main>
</body>
</html>
```